Web Design for Rubbish Removal Company

I am looking for a custom web design that is clean and modern which also has a professional trustworthy feel to it.
The website is http://www.kendrawaste.com.au/ and need:
1 x Front Page
1 x Location Page
Please keep the green colour scheme as this is the corporate colours but would like to steer away from the black.
Industry/Entity Type
It Company
Number of Pages Required
2 page
Font styles to use
Sans Serif
Requirements
Must have
- Clean & Professional
- Keep green colour scheme
Should not have
- Steer away from black
- not look like a template

```html
<!DOCTYPE html>
<html lang="en">
<head>
<meta charset="utf-8">
<title>Kendra Waste Removal</title>
<link href="https://fonts.googleapis.com/css2?family=Open+Sans:wght@400;600;700;800&family=Roboto:wght@400;500;700&display=swap" rel="stylesheet">
<style>
:root{
  --green:#6cbd45;
  --green-light:#8fd061;
  --green-dark:#3f8f2b;
  --green-deep:#2f7420;
  --red:#e1261c;
  --blue:#2b7fd3;
  --yellow:#f6c31c;
  --text:#555;
  --heading:#333;
  --line:#e4e4e4;
  --footer:#3b3d3f;
  --footer-bar:#2f3133;
  --white:#fff;
}
*{box-sizing:border-box;margin:0;padding:0}
html,body{width:1200px;height:4651px;overflow:hidden}
body{font-family:"Open Sans",Arial,sans-serif;color:var(--text);background:var(--white);position:relative;font-size:14px}
.abs{position:absolute}
section,header,footer{position:absolute;left:0;width:1200px}

/* header */
.topbar{top:0;height:93px}
.brand{left:72px;top:20px;font-family:"Open Sans",sans-serif;font-weight:800;font-size:28px;line-height:28px;color:var(--green-dark);letter-spacing:-.5px}
.brand span{display:block}
.contact{right:120px;top:26px;text-align:right}
.contact .phone{font-family:Roboto,sans-serif;font-weight:700;font-size:22px;color:var(--green-dark)}
.contact .email{font-size:13px;color:var(--text)}
.avatar{right:72px;top:22px;width:40px;height:46px;border-radius:4px;background:linear-gradient(#c9a27d,#35506b)}
.nav{top:93px;height:47px;border-top:1px solid var(--line);border-bottom:1px solid var(--line)}
.nav ul{list-style:none;display:flex;position:absolute;left:72px;top:0;height:46px}
.nav li{font-size:13px;font-weight:600;color:var(--text);padding:0 16px;line-height:46px}
.nav li.active{color:var(--green-dark);border-bottom:3px solid var(--green)}
.enquire-btn{right:72px;top:103px;position:absolute;background:var(--red);color:#fff;font-weight:700;font-size:13px;padding:6px 20px;border-radius:16px}

/* hero */
.hero{top:140px;height:567px;background:linear-gradient(120deg,#b8e07a 0%,#7cc642 45%,#4b9d2e 100%)}
.hero-people{left:70px;top:0;width:470px;height:567px;background:linear-gradient(180deg,#e6c4a3 0%,#8bb7d9 55%,#4f9a55 100%);opacity:.55}
.hero-truck{left:640px;top:240px;width:500px;height:330px;background:linear-gradient(180deg,#f3f3f3 0%,#d8d8d8 70%,#6b6b6b 100%);border-radius:6px;opacity:.85}
.hero-title{left:650px;top:78px;color:#fff;text-align:center;width:380px}
.hero-title .small{font-size:22px;font-weight:600}
.hero-title .big{font-family:Roboto,sans-serif;font-size:44px;font-weight:700;line-height:52px}
.badge{left:1035px;top:45px;width:130px;height:130px;border-radius:50%;background:radial-gradient(circle,#f6d34a 55%,#c89415 57%,#f6d34a 70%,#c0201a 72%)}
.features{left:240px;top:500px;width:610px;height:36px;background:rgba(255,255,255,.92);display:flex;justify-content:space-around;align-items:center;font-size:13px;font-weight:600;color:var(--heading)}
.features span{display:flex;align-items:center;gap:5px}

/* services */
.services{top:707px;height:347px}
.section-title{font-weight:800;font-size:22px;line-height:28px;color:var(--heading);text-transform:uppercase}
.underline{width:60px;height:4px;background:var(--green);margin-top:14px}
.services .section-title{position:absolute;left:72px;top:66px;width:240px}
.service{top:59px;width:241px;height:242px;color:#fff;text-align:center}
.service svg{margin-top:40px}
.service h3{font-size:15px;font-weight:700;margin-top:14px;line-height:20px}
.service .more{position:absolute;left:0;bottom:0;width:100%;height:30px;line-height:30px;font-size:12px;font-weight:700;text-align:right;padding-right:16px}
.s-blue{left:344px;background:var(--blue)} .s-blue .more{background:#1f66ac}
.s-yellow{left:614px;background:var(--yellow)} .s-yellow .more{background:#d9a40a}
.s-green{left:886px;background:var(--green)} .s-green .more{background:var(--green-dark)}

/* welcome */
.welcome{top:1079px;height:431px;background:#fff}
.welcome-band{left:0;top:0;width:1200px;height:200px}
.welcome-photo{left:78px;top:62px;width:505px;height:240px;background:linear-gradient(180deg,#b7c9d8 0%,#8a5b48 55%,#9d8c76 100%);border:4px solid #fff}
.welcome-tag{left:840px;top:108px;background:var(--green);color:#fff;font-size:13px;font-weight:700;padding:3px 14px}
.welcome-title{left:650px;top:135px;color:#fff;font-size:34px;font-weight:800;width:480px;text-align:center}
.welcome-text{left:650px;top:222px;width:480px;font-size:14px;line-height:22px;text-align:right}
.link-more{color:var(--green-dark);font-weight:700;font-size:13px}

/* why */
.why{top:1519px;height:564px;background:linear-gradient(90deg,#fff 0%,#f4f4f4 100%)}
.why .section-title{position:absolute;left:72px;top:120px}
.why-list{position:absolute;left:72px;top:190px;width:640px;display:grid;grid-template-columns:1fr 1fr;column-gap:40px;row-gap:30px}
.why-item{display:flex;gap:10px;font-size:15px;line-height:21px;color:var(--heading)}
.why-item svg{flex:none;margin-top:3px}
.why-photo{left:760px;top:20px;width:380px;height:544px;background:linear-gradient(180deg,#f2dc9c 0%,#e6c3a6 35%,#2c2f38 75%)}

/* enquiry */
.enquiry{top:2096px;height:421px;background:linear-gradient(90deg,#2c2f33 0%,#4c5157 45%,#8d8f92 100%)}
.enquiry h2{position:absolute;left:72px;top:80px;width:240px;color:#fff;font-size:24px;font-weight:800;line-height:31px;text-transform:uppercase}
.enquiry p{position:absolute;left:72px;top:210px;width:240px;color:#eee;font-size:14px;line-height:21px}
.form{left:357px;top:92px;width:734px;height:235px;background:rgba(255,255,255,.9);padding:20px 20px}
.field{position:absolute;height:34px;border:1px solid #ccc;background:#fff;font-size:13px;color:#999;padding:7px 12px}
.submit{position:absolute;left:20px;top:185px;width:694px;height:32px;background:var(--green);color:#fff;font-weight:700;font-size:13px;text-align:center;line-height:32px}

/* best price */
.best{top:2517px;height:520px}
.best .section-title{position:absolute;left:72px;top:68px;font-size:22px}
.best-text{left:72px;top:118px;width:680px;font-size:15px;line-height:24px}
.best-text p{margin-bottom:20px}
.best-photo{left:794px;top:78px;width:330px;height:360px;background:linear-gradient(135deg,#6f8a4e 0%,#b23a2c 45%,#3a4452 100%)}
.quote-box{left:223px;top:546px;width:754px;height:190px;border:4px solid var(--green);text-align:center}
.quote-tag{position:absolute;left:50%;transform:translateX(-50%);top:-16px;background:var(--green);color:#fff;font-size:13px;font-weight:700;padding:4px 18px}
.quote-box .lead{margin-top:48px;font-size:21px;font-weight:700;color:var(--heading)}
.quote-box .number{font-family:Roboto,sans-serif;font-size:56px;font-weight:500;color:var(--red);line-height:70px}

/* testimonials */
.customers{top:3224px;height:698px;background:var(--green)}
.customers h2{position:absolute;left:0;width:1200px;top:150px;text-align:center;color:#fff;font-size:24px;font-weight:700;text-transform:uppercase}
.customers .sub{position:absolute;left:350px;width:500px;top:200px;text-align:center;color:#f1ffe6;font-size:15px;line-height:23px}
.person{left:140px;top:300px;width:220px;height:380px;background:linear-gradient(180deg,#d9a682 0%,#5b7fa8 60%,#3d4f66 100%);border-radius:6px}
.testimonial{left:372px;top:300px;width:714px;height:370px;background:rgba(255,255,255,.12);border:1px solid rgba(255,255,255,.35);padding:40px 40px 0 130px;color:#fff}
.qmark{position:absolute;left:40px;top:30px;font-family:Georgia,serif;font-size:90px;line-height:90px;color:#fff;opacity:.8}
.testimonial p{font-size:17px;line-height:27px}
.testimonial .name{margin-top:28px;font-size:22px;font-style:normal}
.testimonial .role{font-size:14px;color:#e7ffd8}
.dots{position:absolute;right:20px;bottom:16px;display:flex;gap:6px}
.dots span{width:18px;height:18px;border-radius:50%;border:2px solid #fff}

/* locations */
.locations{top:3922px;height:427px;background:#fff}
.locations h2{position:absolute;left:0;width:1200px;top:60px;text-align:center;color:var(--heading);font-size:22px;font-weight:800}
.locations .underline{position:absolute;left:570px;top:98px}
.locations .intro{position:absolute;left:350px;width:500px;top:120px;text-align:center;font-size:14px;line-height:22px}
.suburbs{position:absolute;left:78px;top:228px;width:1060px;display:grid;grid-template-columns:repeat(6,1fr);row-gap:10px}
.suburbs li{list-style:none;font-size:14px;color:var(--heading);border-bottom:1px solid var(--line);padding-bottom:8px;margin-right:24px}
.suburbs li::before{content:"• ";color:var(--green)}

/* footer */
.site-footer{top:4349px;height:302px;background:var(--footer);color:#c8c8c8}
.site-footer h4{color:#fff;font-size:16px;font-weight:700;margin-bottom:12px}
.f-about{left:72px;top:40px;width:440px;font-size:13px;line-height:21px}
.f-info{left:590px;top:40px;width:240px;font-size:13px;line-height:21px}
.f-info .reviews{color:var(--green-light)}
.f-pay{left:875px;top:40px;width:260px}
.cards{display:flex;gap:12px}
.cards span{width:64px;height:42px;border-radius:4px}
.footer-bar{left:0;top:240px;width:1200px;height:62px;background:var(--footer-bar);font-size:12px;line-height:62px;padding-left:72px}
.social{position:absolute;right:110px;top:20px;display:flex;gap:8px}
.social span{width:24px;height:24px;border-radius:50%;border:1px solid #9a9a9a}
.to-top{position:absolute;right:72px;top:19px;width:26px;height:26px;background:#555;border-radius:3px}
</style>
</head>
<body>

<header class="topbar">
  <div class="brand abs"><span>KENDRA</span><span>WASTE</span></div>
  <div class="contact abs">
    <div class="phone">0400 555 018</div>
    <div class="email">hello@kendrawaste.com.au</div>
  </div>
  <div class="avatar abs" role="img" aria-label="Portrait of a support contact"></div>
</header>

<nav class="nav" style="position:absolute;left:0;width:1200px">
  <ul>
    <li class="active">HOME</li><li>ABOUT</li><li>SERVICES</li><li>GALLERY</li><li>FAQS</li><li>TESTIMONIALS</li><li>LOCATIONS</li><li>BLOG</li><li>CONTACT</li>
  </ul>
</nav>
<div class="enquire-btn">ENQUIRE NOW</div>

<section class="hero">
  <div class="hero-people abs" role="img" aria-label="Smiling couple giving a thumbs up"></div>
  <div class="hero-truck abs" role="img" aria-label="White company rubbish removal truck"></div>
  <div class="hero-title abs">
    <div class="small">Sydney's Cheapest</div>
    <div class="big">Rubbish Removal</div>
  </div>
  <div class="badge abs" role="img" aria-label="Satisfaction guarantee seal"></div>
  <div class="features abs">
    <span><svg width="14" height="14" viewBox="0 0 14 14"><path d="M2 7l3 3 7-7" stroke="#6cbd45" stroke-width="2.4" fill="none"/></svg>Free Quote</span>
    <span><svg width="14" height="14" viewBox="0 0 14 14"><path d="M2 7l3 3 7-7" stroke="#6cbd45" stroke-width="2.4" fill="none"/></svg>Cheapest Price</span>
    <span><svg width="14" height="14" viewBox="0 0 14 14"><path d="M2 7l3 3 7-7" stroke="#6cbd45" stroke-width="2.4" fill="none"/></svg>Always On-time</span>
    <span><svg width="14" height="14" viewBox="0 0 14 14"><path d="M2 7l3 3 7-7" stroke="#6cbd45" stroke-width="2.4" fill="none"/></svg>Same-day</span>
    <span><svg width="14" height="14" viewBox="0 0 14 14"><path d="M2 7l3 3 7-7" stroke="#6cbd45" stroke-width="2.4" fill="none"/></svg>10+ Years Experience</span>
  </div>
</section>

<section class="services">
  <div class="section-title">Sydney's Cheapest Rubbish Removal Services<div class="underline"></div></div>
  <div class="service s-blue abs">
    <svg width="90" height="84" viewBox="0 0 90 84"><path d="M8 42L45 8l37 34M18 34v44h54V34M38 78V54h14v24" stroke="#fff" stroke-width="5" fill="none" stroke-linejoin="round"/></svg>
    <h3>Household Rubbish<br>Removals</h3>
    <div class="more">FIND OUT MORE »</div>
  </div>
  <div class="service s-yellow abs">
    <svg width="90" height="84" viewBox="0 0 90 84"><rect x="8" y="10" width="74" height="18" stroke="#fff" stroke-width="5" fill="none"/><rect x="14" y="28" width="62" height="48" stroke="#fff" stroke-width="5" fill="none"/><path d="M34 42h22" stroke="#fff" stroke-width="5"/></svg>
    <h3>Office Rubbish<br>Removals</h3>
    <div class="more">FIND OUT MORE »</div>
  </div>
  <div class="service s-green abs">
    <svg width="90" height="84" viewBox="0 0 90 84"><path d="M14 16h62M34 16V8h22v8M20 22l5 56h40l5-56M35 32v38M45 32v38M55 32v38" stroke="#fff" stroke-width="5" fill="none"/></svg>
    <h3>Construction Rubbish<br>Removals</h3>
    <div class="more">FIND OUT MORE »</div>
  </div>
</section>

<section class="welcome">
  <svg class="welcome-band abs" width="1200" height="200" viewBox="0 0 1200 200"><rect width="1200" height="200" fill="#3f8f2b"/><polygon points="0,0 700,0 420,200 0,200" fill="#6cbd45"/><polygon points="700,0 1200,0 1200,90 560,200 420,200" fill="#4fa434"/></svg>
  <div class="welcome-photo abs" role="img" aria-label="Brick house under demolition with rubble"></div>
  <div class="welcome-tag abs">WELCOME TO</div>
  <div class="welcome-title abs">KENDRA WASTE REMOVAL</div>
  <div class="welcome-text abs">
    <p>Kendra Waste offers complete rubbish removal services for your home or business including residential households, offices, retail locations, building sites, demolition and more. We are a trusted Sydney rubbish removal company that handles the most demanding work – and we ensure that your rubbish is always recycled, or removed responsibly.</p>
    <p style="margin-top:14px"><span class="link-more">FIND OUT MORE »</span></p>
  </div>
</section>

<section class="why">
  <div class="section-title">Why choose us?<div class="underline"></div></div>
  <div class="why-list">
    <div class="why-item"><svg width="16" height="16" viewBox="0 0 14 14"><path d="M2 7l3 3 7-7" stroke="#6cbd45" stroke-width="2.4" fill="none"/></svg>Complete rubbish clean-out including demolition, strip outs and labour hire</div>
    <div class="why-item"><svg width="16" height="16" viewBox="0 0 14 14"><path d="M2 7l3 3 7-7" stroke="#6cbd45" stroke-width="2.4" fill="none"/></svg>Removal of white goods, garden rubbish, furniture and more</div>
    <div class="why-item"><svg width="16" height="16" viewBox="0 0 14 14"><path d="M2 7l3 3 7-7" stroke="#6cbd45" stroke-width="2.4" fill="none"/></svg>Extra discounts for returning customers</div>
    <div class="why-item"><svg width="16" height="16" viewBox="0 0 14 14"><path d="M2 7l3 3 7-7" stroke="#6cbd45" stroke-width="2.4" fill="none"/></svg>No job is too large, too small or too difficult</div>
    <div class="why-item"><svg width="16" height="16" viewBox="0 0 14 14"><path d="M2 7l3 3 7-7" stroke="#6cbd45" stroke-width="2.4" fill="none"/></svg>Free quote provided with all enquiries</div>
    <div class="why-item"><svg width="16" height="16" viewBox="0 0 14 14"><path d="M2 7l3 3 7-7" stroke="#6cbd45" stroke-width="2.4" fill="none"/></svg>Over 10 years in the rubbish removal trade</div>
    <div class="why-item"><svg width="16" height="16" viewBox="0 0 14 14"><path d="M2 7l3 3 7-7" stroke="#6cbd45" stroke-width="2.4" fill="none"/></svg>Same-day rubbish and waste collection</div>
    <div class="why-item"><svg width="16" height="16" viewBox="0 0 14 14"><path d="M2 7l3 3 7-7" stroke="#6cbd45" stroke-width="2.4" fill="none"/></svg>CHEAPEST PRICES in Sydney</div>
  </div>
  <div class="why-photo abs" role="img" aria-label="Businesswoman pointing towards the list"></div>
</section>

<section class="enquiry" role="img" aria-label="Office team meeting in the background">
  <h2>Enquire now and receive a call back within 60 minutes!</h2>
  <p>Kendra Waste offers some of the best prices in Sydney. We provide an unrivalled, friendly and affordable, same-day rubbish clean-out to all suburbs in Sydney.</p>
  <div class="form abs">
    <div class="field" style="left:20px;top:20px;width:220px">Name</div>
    <div class="field" style="left:257px;top:20px;width:220px">Email</div>
    <div class="field" style="left:494px;top:20px;width:220px">Phone</div>
    <div class="field" style="left:20px;top:66px;width:694px;height:104px">Message</div>
    <div class="submit">SUBMIT</div>
  </div>
</section>

<section class="best">
  <div class="section-title">Best price rubbish removal</div>
  <div class="best-text abs">
    <p>Kendra Waste offers some of the best prices in Sydney. We provide an unmatched, friendly and affordable, same-day rubbish clean-out to all suburbs in Sydney.</p>
    <p>Our team of experience and on-time rubbish removalists can remove or dispose of household rubbish, garden rubbish, white goods and unwanted household furniture rubbish, bricks, cardboard, concrete, soil and timber rubbish. We also offer affordable removal pricing to builders dealing with specialty items such as strip outs, labour hire, demolition, removal of building site rubbish and waste. We remove rubbish, junk and waste from every suburb of across Sydney's metropolitan area.</p>
    <p>There is no job to big or small for our team. Kendra Waste are a friendly and out-going bunch who are always looking to get the job done. We always clean up after ourselves and ensure we leave your site with happy faces all around. Our team will not leave until you are 110% satisfied with job.</p>
  </div>
  <div class="best-photo abs" role="img" aria-label="Before and after photos of a rubbish pile being cleared"></div>
  <div class="quote-box abs">
    <div class="quote-tag">BEST PRICES IN SYDNEY</div>
    <div class="lead">Grab a free quote with Kendra Waste today by calling</div>
    <div class="number">0400 555 018</div>
  </div>
</section>

<section class="customers">
  <svg class="abs" style="left:0;top:0" width="1200" height="698" viewBox="0 0 1200 698"><polygon points="0,0 520,0 0,420" fill="#7fca52"/><polygon points="0,698 0,420 360,698" fill="#5cae3b"/><polygon points="620,0 1200,0 1200,380" fill="#5fb23d"/><polygon points="1200,698 1200,430 820,698" fill="#7cc64f"/></svg>
  <h2>Happy Customers</h2>
  <div class="sub">At vero eos et accusamus et iusto odio dignissimos ducimus qui blanditiis praesentium voluptatum</div>
  <div class="person abs" role="img" aria-label="Portrait of a satisfied customer"></div>
  <div class="testimonial abs">
    <div class="qmark">“</div>
    <p>Kendra's team did a splendid job with cleaning out our backyard. We had old fridges, computers, microwaves, timber flooring and heaps of other junk left over from our house renovation. They were quick to provide advice and how much it'd cost to get everything cleaned up. They arrived at a time which suited us best and left absolutely no rubbish behind. I can not stress how happy we are now that our family home is junk-free! Thank you!</p>
    <div class="name">Marisa T. - Mascot</div>
    <div class="role">Residential Home Rubbish Removal</div>
    <div class="dots"><span></span><span></span></div>
  </div>
</section>

<section class="locations">
  <h2>LOCATIONS WE SERVICE</h2>
  <div class="underline"></div>
  <div class="intro">Kendra Waste Removal services the entire Sydney region. Some of our serviced areas include:</div>
  <ul class="suburbs">
    <li>Alexandria</li><li>Bondi Junction</li><li>Kensington</li><li>Maroubra</li><li>Potts Point</li><li>Sydney CBD</li>
    <li>Baulkham Hills</li><li>Chatswood</li><li>Kingsford</li><li>Mascot</li><li>Randwick</li><li>Vaucluse</li>
    <li>Bellevue Hill</li><li>Double Bay</li><li>Malabar</li><li>Matraville</li><li>Rose Bay</li><li>Waverly</li>
    <li>Bondi</li><li>Dover Heights</li><li>Marrickville</li><li>Paddington</li><li>St Peters</li><li>Woollahra</li>
  </ul>
</section>

<footer class="site-footer">
  <div class="f-about abs">
    <h4>Kendra Waste Removal</h4>
    <p>Kendra has been in the rubbish removal industry for over 10 years. We specialise in residential rubbish removals, deceased estate clean-ups, building site rubbish removal and have worked with many large rubbish removal organisations in Australia. If you have a rubbish that needs disposing, Kendra can help. Call us for a free quote today.</p>
  </div>
  <div class="f-info abs">
    <h4>Information</h4>
    <p>Sydney, NSW<br>Phone: 0400 555 018<br>Monday through to Sunday, all day.<br><span class="reviews">4.9 stars – 58 reviews on local listings</span></p>
  </div>
  <div class="f-pay abs">
    <h4>Payment Options</h4>
    <div class="cards"><span style="background:#e9e9e9"></span><span style="background:#f0a43a"></span><span style="background:#d6312a"></span></div>
  </div>
  <div class="footer-bar abs">
    Copyright © 2016 Kendra Waste Removal. All rights reserved.
    <div class="social"><span></span><span></span><span></span><span></span><span></span></div>
    <div class="to-top"><svg width="26" height="26" viewBox="0 0 26 26"><path d="M8 15l5-5 5 5" stroke="#fff" stroke-width="2" fill="none"/></svg></div>
  </div>
</footer>

</body>
</html>
```